Design an Outstanding flyer for my company.

I need a flyer designed for our window tinting company based in Brisbane Queensland Australia. The flyer will be targeting Home tinting. We also do mobile car tinting. Something in regards to this could be incorporated into the flyer as well.
I want it to be 2 sided DL size. Black background.
It really needs to Pop, and be a real attention getter.
It needs to be easy to read.
I have provided a mock up with the info on it from our marketing company. It will need a spellcheck etc to make sure everything is correct.
Everything about it can be changed however you like.
I have also included the company logo.

Lets see what you've got!

Target Market(s)

Home Owners

Industry/Entity Type

Home Improvement

Other font styles liked:
• Duan Penh

Requirements
Must have
• All the information on the mock up. Clear and easy to read.
• Must Stand Out!

```html
<!DOCTYPE html>
<html lang="en">
<head>
<meta charset="utf-8">
<title>Brightline Window Tinting – DL Flyer</title>
<link rel="stylesheet" href="https://fonts.googleapis.com/css2?family=Roboto+Condensed:wght@700&family=Lato:ital,wght@0,400;0,700;0,900;1,400&display=swap">
<style>
  :root {
    --page: #ffffff;
    --ink: #0d0d0d;
    --night: #151515;
    --charcoal: #2b2b2b;
    --gold: #f2c21b;
    --gold-deep: #c9961a;
    --gold-pale: #f7dc6a;
    --paper: #ffffff;
    --muted: #d9d9d9;
  }
  * { box-sizing: border-box; margin: 0; padding: 0; }
  html, body { width: 1200px; height: 900px; overflow: hidden; background: var(--page); }
  body { position: relative; font-family: "Lato", sans-serif; }

  .flyer {
    position: absolute;
    width: 370px;
    height: 760px;
    overflow: hidden;
    background: linear-gradient(180deg, var(--charcoal) 0%, var(--night) 55%, var(--ink) 100%);
    box-shadow: 0 2px 6px rgba(0,0,0,0.25);
  }
  .flyer--front { left: 211px; top: 62px; }
  .flyer--back  { left: 637px; top: 66px; }

  .flyer__art { position: absolute; left: 0; top: 0; width: 370px; height: 760px; }

  .brand {
    position: absolute;
    left: 0; width: 100%;
    text-align: center;
    font-family: "Lato", sans-serif;
    font-weight: 700;
    color: var(--gold);
    letter-spacing: 0.5px;
  }
  .brand__mark {
    display: inline-block;
    width: 14px; height: 14px;
    border-radius: 50%;
    background: var(--gold);
    margin-right: 8px;
    vertical-align: -1px;
  }
  .flyer--front .brand { top: 356px; font-size: 19px; }
  .flyer--back .brand  { top: 20px; font-size: 19px; }

  .headline {
    position: absolute;
    left: 0; width: 100%;
    text-align: center;
    font-family: "Roboto Condensed", sans-serif;
    font-weight: 700;
    text-transform: uppercase;
    line-height: 1;
  }
  .headline--gold { color: var(--gold); }
  .headline--white { color: var(--paper); }

  .rule {
    position: absolute;
    height: 2px;
    background: linear-gradient(90deg, transparent, var(--gold-deep) 15%, var(--gold-pale) 50%, var(--gold-deep) 85%, transparent);
  }

  .body-copy {
    position: absolute;
    color: var(--muted);
    font-size: 9.6px;
    line-height: 1.32;
    text-align: justify;
    text-align-last: center;
  }
  .flyer--front .body-copy { left: 32px; width: 306px; top: 548px; font-style: italic; }
  .flyer--back .body-copy  { left: 32px; width: 306px; top: 610px; }

  .reasons {
    position: absolute;
    left: 0; width: 100%;
    text-align: center;
    font-weight: 700;
    text-transform: uppercase;
  }
  .flyer--front .reasons { top: 632px; font-size: 12.5px; line-height: 1.3; color: var(--gold); }
  .flyer--back .reasons  { top: 361px; font-size: 9.5px; color: var(--paper); letter-spacing: 0.2px; }

  .benefit-line {
    position: absolute;
    left: 0; width: 100%;
    text-align: center;
    font-family: "Roboto Condensed", sans-serif;
    font-weight: 700;
    font-size: 19px;
    color: var(--paper);
    top: 522px;
  }
  .benefit-line__accent { color: var(--gold); }

  .gold-band {
    position: absolute;
    left: 0; width: 100%;
    height: 7px;
    background: linear-gradient(90deg, var(--gold-deep), var(--gold-pale) 50%, var(--gold-deep));
  }
  .footer {
    position: absolute;
    left: 0; bottom: 0; width: 100%;
    height: 42px;
    background: var(--paper);
    display: flex; align-items: center; justify-content: center;
    font-weight: 900;
    font-size: 13.5px;
    color: var(--ink);
    letter-spacing: 0.2px;
  }
</style>
</head>
<body>

<!-- Front side -->
<section class="flyer flyer--front">
  <svg class="flyer__art" viewBox="0 0 370 760" aria-hidden="false">
    <defs>
      <linearGradient id="front-photo" x1="0" y1="0" x2="1" y2="1">
        <stop offset="0" stop-color="#6f8fb5"/>
        <stop offset="0.5" stop-color="#2f5d96"/>
        <stop offset="1" stop-color="#1b2a44"/>
      </linearGradient>
      <linearGradient id="front-swoosh" x1="0" y1="0" x2="1" y2="0">
        <stop offset="0" stop-color="#c9961a"/>
        <stop offset="0.5" stop-color="#f7dc6a"/>
        <stop offset="1" stop-color="#c9961a"/>
      </linearGradient>
    </defs>
    <path class="front-top-white" d="M0,0 H370 V8 C230,20 90,110 0,230 Z" fill="#ffffff"/>
    <g role="img" aria-label="Photo of a technician fitting tint film to a car door window">
      <path d="M40,300 C100,140 220,40 370,28 V318 C300,338 220,330 140,304 C100,292 70,292 40,300 Z" fill="url(#front-photo)"/>
    </g>
    <path d="M0,340 C40,160 170,30 370,14" fill="none" stroke="url(#front-swoosh)" stroke-width="7"/>
    <path d="M30,300 C90,262 160,300 230,322 C290,340 335,330 370,315 V330 C330,348 280,352 220,336 C150,316 90,286 30,300 Z" fill="url(#front-swoosh)"/>
  </svg>

  <div class="brand"><span class="brand__mark"></span>Brightline Window Tinting</div>
  <div class="rule" style="left:70px; width:230px; top:400px;"></div>

  <h1 class="headline headline--gold" style="top:408px; font-size:54px;">Save Money</h1>
  <h2 class="headline headline--white" style="top:470px; font-size:29px;">Increase Privacy</h2>

  <p class="benefit-line"><span class="benefit-line__accent">KEEP HEAT OUT</span> BLOCK 99.9% UV RAYS</p>

  <p class="body-copy">reduce glare. reduce energy costs. control the amount of light entering your home. reduce carbon footprint. make home more beautiful. eliminate home hot spots. protect against broken glass. regulate energy. protects upholstery. improve effectiveness of roof insulation. improve health. reduces interior floor fading. eliminate need for blinds. strengthen your windows. insulate in winter. affordable.</p>

  <p class="reasons">20 reasons why home window tinting<br>is perfect for you.</p>

  <div class="gold-band" style="top:711px;"></div>
  <footer class="footer">CALL US 07 3000 4188</footer>
</section>

<!-- Back side -->
<section class="flyer flyer--back">
  <svg class="flyer__art" viewBox="0 0 370 760">
    <defs>
      <linearGradient id="back-photo" x1="0" y1="0" x2="1" y2="1">
        <stop offset="0" stop-color="#e6e6e6"/>
        <stop offset="0.55" stop-color="#b9bdc2"/>
        <stop offset="1" stop-color="#6d7a8c"/>
      </linearGradient>
      <linearGradient id="back-swoosh" x1="0" y1="0" x2="1" y2="0">
        <stop offset="0" stop-color="#c9961a"/>
        <stop offset="0.5" stop-color="#f7dc6a"/>
        <stop offset="1" stop-color="#c9961a"/>
      </linearGradient>
    </defs>
    <rect x="0" y="0" width="370" height="60" fill="#ffffff"/>
    <g role="img" aria-label="Photo of a smiling installer giving a thumbs up beside a silver car in a workshop">
      <path d="M0,40 H370 V268 C300,300 240,305 180,290 C110,272 50,240 0,252 Z" fill="url(#back-photo)"/>
    </g>
    <rect x="0" y="40" width="370" height="30" fill="#ffffff" opacity="0.55"/>
    <path d="M0,250 C60,232 120,268 190,286 C260,304 320,292 370,262 V278 C320,310 255,318 185,300 C115,282 60,252 0,262 Z" fill="url(#back-swoosh)"/>
  </svg>

  <div class="brand"><span class="brand__mark"></span>Brightline Window Tinting</div>

  <p class="reasons">20 reasons why home window tinting is perfect for you.</p>

  <div class="rule" style="left:30px; width:310px; top:397px;"></div>

  <h1 class="headline headline--gold" style="top:414px; font-size:44px;">Keep Heat Out</h1>
  <h2 class="headline headline--white" style="top:466px; font-size:28px;">Block 99.9% UV Rays</h2>
  <h2 class="headline headline--white" style="top:505px; font-size:48px;">Save Money</h2>
  <h3 class="headline headline--white" style="top:558px; font-size:26px;">Increase Privacy</h3>

  <div class="rule" style="left:30px; width:310px; top:592px;"></div>

  <p class="body-copy">reduce glare. reduce energy costs. control the amount of light entering your home. reduce carbon footprint. make home more beautiful. eliminate home hot spots. protect against broken glass. regulate energy. protects upholstery. improve effectiveness of roof insulation. improve health. reduces interior floor fading. eliminate need for blinds. strengthen your windows. insulate in winter. affordable.</p>

  <div class="gold-band" style="top:711px;"></div>
  <footer class="footer">CALL US 07 3000 4188</footer>
</section>

</body>
</html>
```